Business Card Design Project

Mabel's Tonics is a natural skincare business and we need a business card designed. The company focuses on natural products and will be launching with body scrubs and bath fizzies and our mission statement is: To deliver high quality natural beauty products at a good value. It's two cards - one design - the only information changing would be name and email address

Target Market(s)

Females ages 20-50

Industry/Entity Type

Business

Requirements
Must have
• Mabel's Tonics

Corinne Halvorsen-Pitt
T: 800-417-9368
E: Corinne@MabelsTonics.example
W: www.MabelsTonics.example

Ulrich Benedetti
T: 800-417-9368
E: Ulrich@MabelsTonics.example
W: www.MabelsTonics.example
Nice to have
• I'd like to use the colors or text found at www.mabelstonics.example but I'm open to suggestions since design isn't set in stone yet. I would also like to have the words .....a little bit of magic somewhere under the company name in a different type of font. I would like a design that feels clean and maybe a retro feel to it - front and back would be nice but not mandatory

```html
<!DOCTYPE html>
<html lang="en">
<head>
<meta charset="utf-8">
<title>Mabel's Tonics — Business Card</title>
<link href="https://fonts.googleapis.com/css2?family=Fira+Sans:wght@300;400&family=Great+Vibes&display=swap" rel="stylesheet">
<style>
  :root {
    --backdrop: #a8a9ab;
    --card-white: #ffffff;
    --brand-purple: #8a1a84;
    --band-top: #7e1480;
    --band-mid: #5a3c9c;
    --band-bottom: #2f82c8;
    --tagline-grey: #6b6b6b;
    --band-text: #ffffff;
    --rule: rgba(255, 255, 255, 0.55);
    --shadow: rgba(60, 60, 60, 0.45);
  }
  * { margin: 0; padding: 0; box-sizing: border-box; }
  html, body {
    width: 891px;
    height: 1200px;
    overflow: hidden;
    background: var(--backdrop);
  }
  .card {
    position: absolute;
    left: 138px;
    top: 131px;
    width: 618px;
    height: 938px;
    border-radius: 52px;
    background: var(--card-white);
    overflow: hidden;
    box-shadow: 12px 14px 18px var(--shadow);
    font-family: 'Fira Sans', sans-serif;
  }
  .brand-name {
    position: absolute;
    left: 0;
    right: 0;
    top: 125px;
    text-align: center;
    font-family: 'Fira Sans', sans-serif;
    font-weight: 400;
    font-size: 64px;
    letter-spacing: -0.5px;
    color: var(--brand-purple);
  }
  .tagline {
    position: absolute;
    left: 66px;
    top: 220px;
    font-family: 'Great Vibes', cursive;
    font-size: 56px;
    line-height: 40px;
    color: var(--tagline-grey);
  }
  .tagline span { display: block; }
  .tagline .tagline-second { padding-left: 258px; }
  .contact-band {
    position: absolute;
    left: 0;
    right: 0;
    top: 594px;
    bottom: 0;
    background: linear-gradient(to bottom, var(--band-top) 0%, var(--band-mid) 45%, var(--band-bottom) 100%);
    color: var(--band-text);
  }
  .person-name {
    position: absolute;
    left: 66px;
    top: 58px;
    font-weight: 400;
    font-size: 38px;
    line-height: 46px;
  }
  .divider {
    position: absolute;
    left: 66px;
    right: 62px;
    top: 152px;
    border-top: 2px dotted var(--rule);
  }
  .contact-list {
    position: absolute;
    left: 66px;
    top: 176px;
    list-style: none;
    font-weight: 300;
    font-size: 27px;
    line-height: 35px;
  }
</style>
</head>
<body>
  <main class="card">
    <div class="brand-name">Mabel's Tonics</div>
    <p class="tagline">
      <span class="tagline-first">A little bit</span>
      <span class="tagline-second">of magic</span>
    </p>
    <section class="contact-band">
      <h1 class="person-name">Corinne<br>Halvorsen-Pitt</h1>
      <div class="divider"></div>
      <ul class="contact-list">
        <li>T: 800-417-9368</li>
        <li>E: Corinne@MabelsTonics.example</li>
        <li>W: www.MabelsTonics.example</li>
      </ul>
    </section>
  </main>
</body>
</html>
```